Label for Custom Gin Botle

Design an label for Gin botle, need label asap sorry

Target Market(s)

Our customers

Requirements
Must have
• Classic/expensive look

```html
<!DOCTYPE html>
<html lang="nl">
<head>
<meta charset="utf-8">
<title>Halverd Masons Gin – Label</title>
<link rel="stylesheet" href="https://fonts.googleapis.com/css2?family=Arvo:wght@700&family=Lato:wght@400;700&family=Dancing+Script:wght@700&family=Oswald:wght@500&display=swap">
<style>
  :root {
    --backdrop: #0aa57a;
    --label-white: #ffffff;
    --panel-dark: #232323;
    --panel-stripe: #2b2b2b;
    --gold: #d9a520;
    --gold-deep: #a8741a;
    --coral: #ee6a5a;
    --ink-light: #f2f2f2;
    --flora-pink: #f59fd0;
    --flora-yellow: #f7d23a;
    --flora-green: #a9d17a;
    --flora-coral: #f07a64;
    --flora-violet: #b69ad6;
    --flora-aqua: #30e0c8;
  }
  * { box-sizing: border-box; margin: 0; padding: 0; }
  html, body { width: 780px; height: 1200px; overflow: hidden; }
  body { background: var(--backdrop); position: relative; }

  .label {
    position: absolute;
    left: 30px; top: 453px;
    width: 720px; height: 294px;
    background: var(--label-white);
    overflow: hidden;
  }
  .label__flora {
    position: absolute; inset: 0;
    background:
      radial-gradient(circle at 9% 22%, var(--flora-coral) 0 11%, transparent 18%),
      radial-gradient(circle at 14% 88%, var(--flora-aqua) 0 7%, transparent 14%),
      radial-gradient(circle at 30% 48%, var(--flora-violet) 0 5%, transparent 11%),
      radial-gradient(circle at 33% 86%, var(--flora-yellow) 0 8%, transparent 15%),
      radial-gradient(circle at 36% 15%, var(--flora-green) 0 6%, transparent 13%),
      radial-gradient(circle at 56% 10%, var(--flora-yellow) 0 5%, transparent 11%),
      radial-gradient(circle at 74% 24%, var(--flora-yellow) 0 7%, transparent 13%),
      radial-gradient(circle at 72% 60%, var(--flora-pink) 0 8%, transparent 15%),
      radial-gradient(circle at 68% 88%, var(--flora-green) 0 7%, transparent 14%),
      radial-gradient(circle at 92% 20%, var(--flora-green) 0 8%, transparent 15%),
      radial-gradient(circle at 92% 88%, var(--flora-yellow) 0 10%, transparent 17%),
      var(--label-white);
  }

  .badge {
    position: absolute;
    left: 289px; top: 36px;
    width: 141px; height: 258px;
  }
  .badge__frame { position: absolute; left: 0; top: 0; width: 141px; height: 216px; }
  .badge__ornament {
    position: absolute; left: 33px; top: 10px; width: 75px; height: 30px;
    background: linear-gradient(180deg, var(--gold), var(--gold-deep));
    border-radius: 40% 40% 30% 30%;
    opacity: .85;
  }
  .badge__name {
    position: absolute; left: 0; right: 0; top: 48px;
    text-align: center;
    font-family: "Arvo", Georgia, serif; font-weight: 700;
    font-size: 21px; letter-spacing: .5px;
    color: var(--gold);
  }
  .badge__bracket { position: absolute; left: 12px; top: 70px; width: 117px; height: 12px; }
  .badge__line {
    position: absolute; left: 0; right: 0; top: 92px;
    text-align: center;
    font-family: "Lato", Arial, sans-serif; font-weight: 700;
    font-size: 13px; letter-spacing: .5px;
    color: var(--ink-light);
  }
  .badge__spirit {
    position: absolute; left: 18px; top: 100px;
    font-family: "Dancing Script", cursive; font-weight: 700;
    font-size: 64px; line-height: 1;
    color: var(--gold);
  }
  .badge__variant {
    position: absolute; left: 67px; top: 155px;
    font-family: "Lato", Arial, sans-serif;
    font-size: 9px; letter-spacing: .3px;
    color: var(--ink-light);
  }
  .badge__volume {
    position: absolute; left: 66px; top: 166px;
    font-family: "Oswald", Arial, sans-serif; font-weight: 500;
    font-size: 4.6px; letter-spacing: .4px;
    color: var(--ink-light);
  }
  .badge__laurel {
    position: absolute; left: 40px; top: 180px; width: 62px; height: 12px;
    background: linear-gradient(90deg, var(--gold-deep), #7a3a1a, var(--gold-deep));
    border-radius: 50%;
    opacity: .8;
  }
  .badge__info {
    position: absolute; left: 14px; top: 209px;
    width: 114px; height: 49px;
    background: var(--coral);
    padding: 5px 4px;
  }
  .badge__legal {
    font-family: "Oswald", Arial, sans-serif; font-weight: 500;
    font-size: 3.6px; line-height: 1.15; letter-spacing: .2px;
    color: var(--ink-light); text-transform: uppercase;
    position: absolute; left: 4px; bottom: 3px;
  }
  .badge__icons { position: absolute; right: 4px; bottom: 4px; display: flex; gap: 2px; }
  .badge__icon { width: 11px; height: 10px; border: 1px solid var(--ink-light); }
</style>
</head>
<body>
  <section class="label">
    <div class="label__flora" role="img" aria-label="Hand-drawn botanical illustration of colourful tropical flowers, palm leaves, berries and foliage in coral, pink, yellow, green, violet and aqua"></div>

    <div class="badge">
      <svg class="badge__frame" viewBox="0 0 141 216" aria-hidden="true">
        <defs>
          <pattern id="stripes" width="8" height="8" patternUnits="userSpaceOnUse">
            <rect width="8" height="8" fill="#232323"/>
            <rect width="4" height="8" fill="#2b2b2b"/>
          </pattern>
        </defs>
        <path d="M16 14 Q16 4 26 4 L115 4 Q125 4 125 14 Q125 22 135 24 L137 24 L137 186 Q137 212 70.5 212 Q4 212 4 186 L4 24 L6 24 Q16 22 16 14 Z"
              fill="url(#stripes)" stroke="#d9a520" stroke-width="3"/>
      </svg>
      <div class="badge__ornament" role="img" aria-label="Gold scroll ornament with a central leaf"></div>
      <div class="badge__name">HALVERD</div>
      <svg class="badge__bracket" viewBox="0 0 117 12" aria-hidden="true">
        <path d="M2 0 V9 H115 V0" fill="none" stroke="#ffffff" stroke-width="3"/>
      </svg>
      <div class="badge__line">MASONS</div>
      <div class="badge__spirit">gin</div>
      <div class="badge__variant">ORIGINAL</div>
      <div class="badge__volume">40% VOL. &nbsp;|&nbsp; 500ML</div>
      <div class="badge__laurel" role="img" aria-label="Small laurel branch ornament"></div>
      <div class="badge__info">
        <p class="badge__legal">Kan sporen van<br>allergenen bevatten<br>Lindenkade 7<br>1234 AB Veldhoven<br>info@halverd-gin.com</p>
        <div class="badge__icons"><span class="badge__icon"></span><span class="badge__icon"></span></div>
      </div>
    </div>
  </section>
</body>
</html>
```